Home Automation Company needs DL size flyer design

We need a flyer that looks like a home control touch panel page on a smartphone. Similar to a "Lumora9" home page. The company is Based in Sydney and named "Halvestry". We integrate home systems into one central control. Lights, Power, Audio/Visual, Cameras, Security, Access Control, Media Storage. We are inviting people to have their future home now. Looking at new company Logo similar to "Trellis Quarterly"

Target Market(s)

Home Owners Eastern Suburbs Sydney

Industry/Entity Type

Home Improvement

Contact Information for Business Card

Possibly mini Smartphone look like flyer.

Font styles to use
Other font styles liked:
• TP Black Extended

Colors
cadf82
ffffff
86cfc6
f59195

Requirements
Must have
• A few Media Streaming Services Logos
• Promote ease of use and lifestyle enhancement.
• Security of Home, "Peace of mind" focus.
Nice to have
• Pictures of "Press buttons for services available"
• Home control in one app. remote access from anywere.

```html
<!DOCTYPE html>
<html lang="en">
<head>
<meta charset="utf-8">
<title>Halvestry – DL Flyers</title>
<link href="https://fonts.googleapis.com/css2?family=Michroma&family=PT+Sans:wght@400;700&family=Roboto:wght@300;400;700&display=swap" rel="stylesheet">
<style>
  :root {
    --brand-red: #c8161d;
    --deep-red: #9e1015;
    --ink: #222222;
    --grey-text: #4a4a4a;
    --page-bg: #3a3a3a;
    --white: #ffffff;
  }
  * { box-sizing: border-box; margin: 0; padding: 0; }
  html, body { width: 1200px; height: 1150px; overflow: hidden; }
  body { background: var(--page-bg); position: relative; font-family: "PT Sans", sans-serif; }

  .flyer {
    position: absolute; top: 106px; width: 450px; height: 940px;
    background: var(--white); overflow: hidden;
    box-shadow: 0 6px 24px rgba(0,0,0,.45);
  }
  .flyer--services { left: 98px; }
  .flyer--features { left: 654px; }

  .layer { position: absolute; inset: 0; }
  .photo { position: absolute; }
  .photo--interior {
    left: 0; top: 110px; width: 450px; height: 720px;
    background: linear-gradient(180deg, #e9e9e9 0%, #f3f3f3 40%, #dcdcdc 75%, #cfcfcf 100%);
  }
  .photo--street {
    left: 0; top: 110px; width: 450px; height: 530px;
    background: linear-gradient(160deg, #8d8f92 0%, #b3b3b0 35%, #7e7a72 60%, #55524e 100%);
  }
  .photo--tablet {
    left: 150px; top: 597px; width: 262px; height: 202px; border-radius: 12px;
    background: linear-gradient(180deg, #f4f4f4 0%, #e2e2e2 100%);
    box-shadow: 0 4px 14px rgba(0,0,0,.3);
  }
  .photo--tablet::after {
    content: ""; position: absolute; left: 24px; top: 18px; right: 24px; bottom: 22px;
    background: linear-gradient(135deg, #3b3b3b, #6b6256 50%, #2e3238);
  }
  .photo--panel {
    left: -2px; top: 426px; width: 144px; height: 144px; border-radius: 50%;
    border: 4px solid var(--white);
    background: linear-gradient(135deg, #d9d9d9 0%, #2b2d33 35%, #1d1f24 70%, #c9c9c9 100%);
    box-shadow: 0 3px 10px rgba(0,0,0,.35);
  }

  .brand { position: absolute; top: 40px; left: 0; width: 100%; text-align: center; }
  .brand__name {
    font-family: "Michroma", sans-serif; font-size: 38px; line-height: 1;
    color: var(--ink); letter-spacing: 2px;
  }
  .brand__tagline {
    font-family: "Roboto", sans-serif; font-weight: 300; font-size: 30px;
    color: var(--grey-text); margin-top: 6px; letter-spacing: .5px;
  }

  .intro {
    position: absolute; top: 198px; left: 0; width: 450px; text-align: center;
    font-family: "Roboto", sans-serif; font-weight: 300; font-size: 19.5px; line-height: 23px;
    color: var(--brand-red);
  }

  .services-tab {
    position: absolute; left: 0; top: 285px; width: 214px; height: 40px;
    background: linear-gradient(180deg, #d21c22, var(--deep-red));
    border-radius: 0 14px 14px 0;
    color: var(--white); font-family: "Roboto", sans-serif; font-size: 19px;
    line-height: 40px; padding-left: 16px;
  }
  .services-list {
    position: absolute; left: 31px; top: 334px; width: 404px; list-style: none;
    font-size: 13px; line-height: 18px; color: #1e1e1e;
  }
  .services-list li { position: relative; }
  .services-list li::before {
    content: ""; position: absolute; left: -13px; top: 6px; width: 5px; height: 5px;
    border-radius: 50%; border: 2px solid var(--brand-red);
  }

  .contact-pill {
    position: absolute; left: 26px; top: 827px; width: 424px; height: 53px;
    border-radius: 27px 0 0 27px;
    background: linear-gradient(180deg, #ffffff 0%, #e6e6e6 70%, #cfcfcf 100%);
    display: flex; align-items: center; justify-content: center; gap: 20px;
    font-family: "Roboto", sans-serif; font-weight: 700; font-size: 20px; color: #111;
  }
  .contact-pill span { display: inline-flex; align-items: center; gap: 7px; }
  .contact-pill svg { width: 12px; height: 14px; }
  .web {
    position: absolute; left: 0; top: 888px; width: 450px; text-align: center;
    font-family: "Roboto", sans-serif; font-size: 21px; letter-spacing: 1.6px; color: var(--white);
  }

  .headline {
    position: absolute; right: 20px; top: 484px; width: 320px; text-align: right;
    font-family: "Roboto", sans-serif; font-weight: 300; color: var(--white);
  }
  .headline__main { font-size: 21px; line-height: 26px; }
  .headline__sub { font-size: 19px; line-height: 23px; margin-top: 6px; }
  .features {
    position: absolute; left: 27px; top: 600px; width: 403px;
    font-size: 12.4px; line-height: 14px; color: var(--white); text-align: justify;
  }
  .features p + p { margin-top: 14px; }
</style>
</head>
<body>

<section class="flyer flyer--services">
  <div class="photo photo--interior" role="img" aria-label="Soft white living room interior with pendant light and lounge chairs"></div>

  <svg class="layer" viewBox="0 0 450 940" aria-hidden="true">
    <defs>
      <linearGradient id="redFadeA" x1="0" y1="0" x2="1" y2="1">
        <stop offset="0" stop-color="#d01a20"/>
        <stop offset="1" stop-color="#9a0f14"/>
      </linearGradient>
    </defs>
    <path d="M0,120 Q225,215 450,128 L450,136 Q225,225 0,132 Z" fill="#c9c9c9"/>
    <path d="M0,0 H450 V128 Q225,215 0,120 Z" fill="#ffffff"/>
    <path d="M0,800 Q190,628 450,612 L450,620 Q200,640 0,808 Z" fill="#e4e4e4"/>
    <path d="M0,808 Q200,640 450,620 V940 H0 Z" fill="url(#redFadeA)"/>
  </svg>

  <header class="brand">
    <div class="brand__name">HALVESTRY</div>
    <div class="brand__tagline">shape your home</div>
  </header>

  <p class="intro">Technology and Décor Combined<br>You and your home in Sync<br>Shape your Home now and live smarter</p>

  <div class="services-tab">Services including</div>
  <ul class="services-list">
    <li>Main/Sub Boards and Automation (smart home) controllers.</li>
    <li>Telephone, Data/Internet setup, TV, CCTV, Intercom/PABX</li>
    <li>Home theatre, multi room audio, sources central or local. Speakers.</li>
    <li>Multi room, music or video in any or all room flexibility. Coupled with high quality audio and HD video.</li>
    <li>Touch Panels (in wall or wireless), Monitors, OLED, LCD, LED Televisions</li>
    <li>Movement detectors for lighting, flood lighting.</li>
    <li>Stainless/Glass/Stone power and light switches.</li>
    <li>Alarm systems, detectors</li>
    <li>CCTV Camera styles. Indoor/Outdoor IP/analogue</li>
    <li>Windows, Awnings, Blinds control (wind rain sensors)</li>
    <li>Light fittings, LED lighting, specifications and design.</li>
    <li>Risers and cabling access.</li>
    <li>Floor heating, Air Conditioning</li>
  </ul>

  <div class="photo photo--tablet" role="img" aria-label="Hands holding a white tablet showing a room-by-room home control app"></div>

  <div class="contact-pill">
    <span><svg viewBox="0 0 12 14"><rect x="2" y="0.5" width="8" height="13" rx="1.5" fill="none" stroke="#c8161d" stroke-width="1.5"/><circle cx="6" cy="11" r=".9" fill="#c8161d"/></svg>0412 680 315</span>
    <span><svg viewBox="0 0 14 14"><path d="M3 1 L5.5 1 L6.5 4.2 L5 5.3 Q6.3 8 8.7 9 L9.8 7.5 L13 8.5 L13 11 Q12 13 9.5 12.6 Q2.5 10.5 1.4 3.5 Q1.2 1.5 3 1 Z" fill="#c8161d"/></svg>(612) 9488-2061</span>
  </div>
  <div class="web">www.halvestry.com.au</div>
</section>

<section class="flyer flyer--features">
  <div class="photo photo--street" role="img" aria-label="City street with yellow taxis and a hand holding a smartphone running a home control app"></div>

  <svg class="layer" viewBox="0 0 450 940" aria-hidden="true">
    <defs>
      <linearGradient id="redFadeB" x1="0" y1="0" x2="1" y2="1">
        <stop offset="0" stop-color="#d01a20"/>
        <stop offset="1" stop-color="#9a0f14"/>
      </linearGradient>
    </defs>
    <path d="M0,120 Q225,215 450,128 L450,136 Q225,225 0,132 Z" fill="#c9c9c9"/>
    <path d="M0,0 H450 V128 Q225,215 0,120 Z" fill="#ffffff"/>
    <path d="M0,608 Q130,452 450,430 L450,446 Q150,462 0,624 Z" fill="#e6e6e6"/>
    <path d="M0,624 Q150,462 450,446 V940 H0 Z" fill="url(#redFadeB)"/>
  </svg>

  <header class="brand">
    <div class="brand__name">HALVESTRY</div>
    <div class="brand__tagline">shape your home</div>
  </header>

  <div class="photo photo--panel" role="img" aria-label="Finger pressing an in-wall touch panel showing home control buttons"></div>

  <div class="headline">
    <div class="headline__main">Peace of mind</div>
    <div class="headline__sub">Home control in one app. remote<br>access from anywhere</div>
  </div>

  <div class="features">
    <p>Décor-Friendly Gadgets. Home automation technology can blend in better with your décor</p>
    <p>Wireless Power Controls. Home automation allows you to control myriad devices with the touch of your finger.</p>
    <p>Automated Door Locks. If you're carrying heavy grocery bags or a crying child, unlocking your door can be quite a feat. Smart locks take the guesswork out of using a key by automating your front door to unlock or even open as you approach.</p>
    <p>Advanced Security Systems. Watch your kids get home safely from school, make sure they're doing their homework and not watching TV, or simply set up and arm your security system and other alarms while you're away with the touch of a button.</p>
  </div>

  <div class="contact-pill">
    <span><svg viewBox="0 0 12 14"><rect x="2" y="0.5" width="8" height="13" rx="1.5" fill="none" stroke="#c8161d" stroke-width="1.5"/><circle cx="6" cy="11" r=".9" fill="#c8161d"/></svg>0412 680 315</span>
    <span><svg viewBox="0 0 14 14"><path d="M3 1 L5.5 1 L6.5 4.2 L5 5.3 Q6.3 8 8.7 9 L9.8 7.5 L13 8.5 L13 11 Q12 13 9.5 12.6 Q2.5 10.5 1.4 3.5 Q1.2 1.5 3 1 Z" fill="#c8161d"/></svg>(612) 9488-2061</span>
  </div>
  <div class="web">www.halvestry.com.au</div>
</section>

</body>
</html>
```